Building showcase catalogue for a post frame construction company

We are looking for a brochure for our clients showcasing our buildings. We are a post frame building company that makes commercial, ag, homes, and other building types. We are looking for a brochure that we can use with all the types of buildings simply by changing out the pictures. We would like a more photo heavy brochure thats 1-5 pages. We want the design to feel high end luxury. Our colors are black, white, and chrome. I will upload our logo as well as some building photos in the suburban category of our buildings. We would like a page to showcase some building layouts as well.

We need the size to be us letter size.

Industry/Entity Type

Construction

Font styles to use
Serif

Colors

Designer to choose only greyscale colors for use in the design.

Requirements
Must have
• A space to showcase building photos, small text space for information. An area to showcase building layouts.
Nice to have
• I would like to have a very clean professional look thats looks high end.
Should not have
• Areas for detail pictures. We mostly have exterior building shots.

```html
<!DOCTYPE html>
<html lang="en">
<head>
<meta charset="utf-8">
<title>Ridgeline Post Frame – Building Showcase Brochure</title>
<link href="https://fonts.googleapis.com/css2?family=Montserrat:wght@500;700;800;900&family=Open+Sans:wght@400;600;700&display=swap" rel="stylesheet">
<style>
  :root{
    --stage:#e4e4e4;
    --black:#111111;
    --charcoal:#1d1d1d;
    --graphite:#2c2c2c;
    --steel:#6f6f6f;
    --chrome:#c9c9c9;
    --paper:#ffffff;
    --paper-soft:#f2f2f2;
    --ink:#222222;
    --muted:#9a9a9a;
    --shadow:0 18px 40px rgba(0,0,0,.22);
  }
  *{box-sizing:border-box;margin:0;padding:0}
  html,body{width:1200px;height:3648px;overflow:hidden}
  body{background:var(--stage);position:relative;font-family:"Open Sans",Arial,sans-serif;color:var(--ink)}

  .sheet{position:absolute;box-shadow:var(--shadow);overflow:hidden}
  .sheet--single{left:325px;width:550px;height:712px}
  .sheet--spread{left:50px;width:1100px;height:712px;display:flex}
  .page{position:relative;width:550px;height:712px;overflow:hidden}
  .page + .page{border-left:1px solid rgba(0,0,0,.25)}

  .photo{position:absolute;background:linear-gradient(180deg,#b7cde0 0%,#cfd9df 42%,#9a3a38 43%,#8d3533 66%,#8c9672 67%,#6d7556 100%)}
  .photo--home{background:linear-gradient(180deg,#c5d3e0 0%,#dfe5ea 40%,#f1f1f1 41%,#d6d6d6 70%,#a9a9a3 71%,#8e8e88 100%)}
  .photo--shop{background:linear-gradient(180deg,#555 0%,#6b6b6b 35%,#8f2d2b 60%,#4a4a4a 61%,#9a9a9a 100%)}
  .photo--room{background:linear-gradient(160deg,#c9a27a 0%,#a77a52 45%,#e5d8c6 46%,#b9a48a 100%)}
  .photo--framed{border:6px solid var(--paper)}

  /* cover */
  .cover{background:var(--charcoal);color:var(--paper)}
  .cover__texture{position:absolute;inset:0;background:repeating-linear-gradient(135deg,rgba(255,255,255,.025) 0 2px,transparent 2px 6px)}
  .brand{display:flex;align-items:center;justify-content:center;gap:8px;font-family:"Montserrat",sans-serif;font-weight:800;letter-spacing:.14em;text-transform:uppercase;color:var(--paper)}
  .brand__mark{width:14px;height:14px;background:var(--paper)}
  .cover .brand{position:absolute;top:34px;left:0;right:0;font-size:13px}
  .cover__title{position:absolute;top:70px;left:0;right:0;text-align:center;font-family:"Montserrat",sans-serif;font-weight:900;font-size:74px;letter-spacing:.02em;line-height:1}
  .cover__subtitle{position:absolute;top:150px;left:0;right:0;text-align:center;font-family:"Montserrat",sans-serif;font-weight:600;font-size:21px;line-height:1.2;letter-spacing:.03em;text-transform:uppercase}
  .cover .photo{top:232px;left:70px;width:410px;height:250px}
  .cover__stripes{position:absolute;left:0;top:430px;width:550px;height:230px}
  .cover__url{position:absolute;left:24px;top:520px;transform:rotate(-90deg);transform-origin:left top;font-size:10px;letter-spacing:.28em;color:var(--chrome);white-space:nowrap}
  .cover__base{position:absolute;left:0;bottom:0;width:100%;height:52px;background:var(--black)}

  /* back cover */
  .back{background:var(--paper)}
  .back__top{position:absolute;inset:0 0 270px 0;background:var(--charcoal);color:var(--paper);padding:44px 46px 0}
  .back .brand{font-size:12px;margin-bottom:34px}
  .back__text{font-size:11px;line-height:1.75;color:#d8d8d8;text-align:justify}
  .follow{position:absolute;left:0;top:400px;width:300px;height:64px;background:var(--paper);padding:10px 46px}
  .follow__title{font-family:"Montserrat",sans-serif;font-weight:800;font-size:15px;color:var(--ink)}
  .follow__icons{display:flex;gap:6px;margin-top:6px}
  .follow__icons span{width:18px;height:18px;background:var(--ink)}
  .contact{position:absolute;left:46px;right:46px;bottom:48px;display:grid;grid-template-columns:1fr 1fr 1fr;gap:18px;border-top:2px solid var(--ink);padding-top:18px}
  .contact__head{grid-column:1/-1;font-family:"Montserrat",sans-serif;font-weight:800;font-size:14px;text-transform:uppercase;letter-spacing:.08em}
  .contact__item{font-size:10.5px;line-height:1.6;display:flex;gap:8px}
  .contact__item svg{flex:none;margin-top:2px}
  .contact__item b{display:block;font-weight:700;font-size:11px}

  /* inner pages */
  .inner--dark{background:var(--charcoal);color:#e2e2e2}
  .inner--light{background:var(--paper-soft);color:var(--ink)}
  .tag{position:absolute;background:var(--paper);color:var(--ink);font-family:"Montserrat",sans-serif;font-weight:800;font-size:12px;letter-spacing:.08em;text-transform:uppercase;padding:6px 14px}
  .tag--dark{background:var(--black);color:var(--paper)}
  .copy{position:absolute;font-size:10px;line-height:1.65;text-align:justify}
  .copy h3{font-family:"Montserrat",sans-serif;font-size:12px;font-weight:800;text-transform:uppercase;letter-spacing:.06em;margin-bottom:6px}
  .band{position:absolute;left:0;right:0;background:var(--black)}
</style>
</head>
<body>

<!-- Front cover -->
<section class="sheet sheet--single">
  <article class="page cover">
    <div class="cover__texture"></div>
    <div class="brand"><span class="brand__mark"></span>Ridgeline Post Frame</div>
    <h1 class="cover__title">BUILDING</h1>
    <p class="cover__subtitle">Commercial, Ag, Homes<br>and Other Building</p>
    <svg class="cover__stripes" viewBox="0 0 550 230" aria-hidden="true">
      <rect width="550" height="230" fill="#262626"/>
      <polygon points="0,230 0,120 550,40 550,110 120,230" fill="#3a3a3a"/>
      <line x1="0" y1="150" x2="550" y2="68" stroke="#d9d9d9" stroke-width="3"/>
      <line x1="0" y1="172" x2="550" y2="90" stroke="#8a8a8a" stroke-width="2"/>
    </svg>
    <div class="photo photo--framed" role="img" aria-label="Red post frame garage building with open doors on a gravel drive"></div>
    <div class="cover__url">www.ridgelinepostframe.com</div>
    <div class="cover__base"></div>
  </article>
</section>

<!-- Back cover and front cover spread -->
<section class="sheet sheet--spread" style="top:872px">
  <article class="page back">
    <div class="back__top">
      <div class="brand"><span class="brand__mark"></span>Ridgeline Post Frame</div>
      <p class="back__text">Ridgeline Post Frame designs and raises commercial halls, farm shops, homes and garages across the region. Each project starts with a plan shaped around the site and the way the space will be used, then moves through careful framing, clean steel work and a finished shell built to last for decades. Our crews handle every stage in house, so the quality you see on day one holds for years to come. We welcome every question and are glad to walk any client through past builds.</p>
    </div>
    <div class="follow">
      <div class="follow__title">Follow Us on</div>
      <div class="follow__icons"><span></span><span></span><span></span></div>
    </div>
    <div class="contact">
      <div class="contact__head">Contact Us</div>
      <div class="contact__item">
        <svg width="14" height="14" viewBox="0 0 24 24"><path d="M6.6 10.8a15 15 0 0 0 6.6 6.6l2.2-2.2a1 1 0 0 1 1-.25 11.4 11.4 0 0 0 3.6.6 1 1 0 0 1 1 1V20a1 1 0 0 1-1 1A17 17 0 0 1 3 4a1 1 0 0 1 1-1h3.5a1 1 0 0 1 1 1c0 1.25.2 2.45.6 3.6a1 1 0 0 1-.25 1z" fill="#222"/></svg>
        <div><b>Phone</b>(555) 014-2280</div>
      </div>
      <div class="contact__item">
        <svg width="14" height="14" viewBox="0 0 24 24"><rect x="2" y="5" width="20" height="14" fill="none" stroke="#222" stroke-width="2"/><path d="M2 6l10 7 10-7" fill="none" stroke="#222" stroke-width="2"/></svg>
        <div><b>Email</b>hello@ridgelinepostframe.com</div>
      </div>
      <div class="contact__item">
        <svg width="14" height="14" viewBox="0 0 24 24"><path d="M12 2a7 7 0 0 0-7 7c0 5 7 13 7 13s7-8 7-13a7 7 0 0 0-7-7zm0 9.5A2.5 2.5 0 1 1 12 6.5a2.5 2.5 0 0 1 0 5z" fill="#222"/></svg>
        <div><b>Address</b>418 Mill Creek Road<br>Harlow Valley</div>
      </div>
    </div>
  </article>
  <article class="page cover">
    <div class="cover__texture"></div>
    <div class="brand"><span class="brand__mark"></span>Ridgeline Post Frame</div>
    <h2 class="cover__title">BUILDING</h2>
    <p class="cover__subtitle">Commercial, Ag, Homes<br>and Other Building</p>
    <svg class="cover__stripes" viewBox="0 0 550 230" aria-hidden="true">
      <rect width="550" height="230" fill="#262626"/>
      <polygon points="0,230 0,120 550,40 550,110 120,230" fill="#3a3a3a"/>
      <line x1="0" y1="150" x2="550" y2="68" stroke="#d9d9d9" stroke-width="3"/>
      <line x1="0" y1="172" x2="550" y2="90" stroke="#8a8a8a" stroke-width="2"/>
    </svg>
    <div class="photo photo--framed" role="img" aria-label="Red post frame garage building with open doors on a gravel drive"></div>
    <div class="cover__url">www.ridgelinepostframe.com</div>
    <div class="cover__base"></div>
  </article>
</section>

<!-- Showcase spread one -->
<section class="sheet sheet--spread" style="top:1744px">
  <article class="page inner--dark">
    <div class="tag" style="left:40px;top:34px">Custom Homes</div>
    <p class="copy" style="left:40px;right:40px;top:76px">Every frame we raise is engineered for strength and long service, with clean lines, tight details and finishes chosen to suit the land, the work and the way our clients live. Open spans give room to grow without interior posts.</p>
    <div class="photo photo--home photo--framed" style="left:40px;top:168px;width:470px;height:360px" role="img" aria-label="White farmhouse style post frame home with gabled porch"></div>
    <div class="band" style="top:560px;height:152px"></div>
    <p class="copy" style="left:40px;right:40px;top:584px;color:#cfcfcf"><span style="display:block;font-family:Montserrat,sans-serif;font-weight:800;font-size:12px;color:#fff;letter-spacing:.06em;text-transform:uppercase;margin-bottom:6px">Home Layout</span>Three bedrooms, two baths and an attached shop under one roofline. Vaulted great room, covered porch and full steel exterior with a lifetime finish.</p>
  </article>
  <article class="page inner--dark">
    <div class="photo photo--room photo--framed" style="left:34px;top:34px;width:230px;height:190px" role="img" aria-label="Finished interior living space of a post frame building"></div>
    <div class="tag" style="left:290px;top:40px">Suburban</div>
    <p class="copy" style="left:290px;right:34px;top:80px">Finished living areas sit inside the same sturdy frame, with tall ceilings, wide windows and warm wood trim throughout the main floor.</p>
    <p class="copy" style="left:34px;width:230px;top:262px">A classic red shop with white trim, built for tractors, tools and the seasons ahead. Large sliding doors open the full width for easy access.</p>
    <div class="photo photo--framed" style="left:290px;top:250px;width:226px;height:200px" role="img" aria-label="Red post frame shop with white trim beside a stone path"></div>
    <div class="photo photo--shop photo--framed" style="left:34px;top:478px;width:270px;height:200px" role="img" aria-label="Open garage bay with a red tractor parked inside"></div>
    <div class="tag" style="left:330px;top:490px">Ag Buildings</div>
    <p class="copy" style="left:330px;right:34px;top:530px">Clear span bays store equipment and feed with room to spare, and insulated walls keep the work going in every season of the year.</p>
  </article>
</section>

<!-- Showcase spread two -->
<section class="sheet sheet--spread" style="top:2616px">
  <article class="page inner--light">
    <div class="tag tag--dark" style="left:40px;top:34px">Commercial</div>
    <div class="photo photo--home" style="left:40px;top:74px;width:300px;height:190px" role="img" aria-label="Two storey commercial post frame building with balcony"></div>
    <p class="copy" style="left:360px;right:34px;top:80px">Bold office fronts and showrooms that open straight into a working shop space behind.</p>
    <div class="tag tag--dark" style="left:360px;top:290px">Shop Homes</div>
    <div class="photo photo--home" style="left:40px;top:290px;width:300px;height:180px" role="img" aria-label="Long grey post frame shop home with dark roof"></div>
    <p class="copy" style="left:360px;right:34px;top:330px">Living quarters and a full work bay joined under a single long roof.</p>
    <div class="tag tag--dark" style="left:40px;top:498px">Garages</div>
    <div class="photo photo--framed" style="left:40px;top:536px;width:300px;height:150px;border-color:#111" role="img" aria-label="Red and white post frame garage on a green lawn"></div>
    <p class="copy" style="left:360px;right:34px;top:540px">Detached garages in any size, finished to match the home beside them.</p>
  </article>
  <article class="page inner--dark">
    <div class="tag" style="left:34px;top:34px">Lake Homes</div>
    <p class="copy" style="left:34px;width:240px;top:76px">Timber interiors with open lofts and tall glass walls bring the view inside every room of the house.</p>
    <div class="photo photo--room photo--framed" style="left:296px;top:34px;width:220px;height:200px" role="img" aria-label="Timber lined loft interior of a post frame lake home"></div>
    <div class="photo photo--home photo--framed" style="left:34px;top:262px;width:482px;height:330px" role="img" aria-label="Large white post frame home with black framed windows"></div>
    <p class="copy" style="left:34px;right:34px;top:612px">Every frame we raise is engineered for strength and long service, with clean lines, tight details and finishes chosen to suit the land, the work and the way our clients live.</p>
  </article>
</section>

</body>
</html>
```